Mediation service showing compassion, collaboration, and resolution

I would like to purchase a customized version of a design you have previously submitted - https://www.pixelbidhub.com/design/48172635

Hello,

I would like a design for a flyer for my mediation business.
I also want to include a message that says that I offer rates on sliding scale.
My website is: www.morvantelkresolve.com

Let me know what other details you might want?

Thank you,

Teodric

Target Market(s)

Local community, western Massachusetts USA. Businesses, families, individuals.

Industry/Entity Type

Mediation, Legal, Alternative Dispute Resolution, Divorce, Unions

Font styles to use
Sans Serif

Colors
0094D4
00A9DD
6FCCEA
C7EBF8
E9F6FB
00AB8E
00BBA5
67D7C9
C6EFE9
E9F9F6

Requirements
Must have
• “Sliding scale rates available “. Phone and email details. +1.555.384.7290 and email: teodric@morvantelkresolve.com as well as we code to my website www.morvantelkresolve.com

```html
<!DOCTYPE html>
<html lang="en">
<head>
<meta charset="utf-8">
<title>Teodric F. Morvantelk – Mediation Flyer</title>
<link href="https://fonts.googleapis.com/css2?family=Kalam:wght@700&family=Poppins:wght@400;500&family=Montserrat:wght@600&display=swap" rel="stylesheet">
<style>
  :root {
    --paper: #fdedf5;
    --green-deep: #00a587;
    --green-bright: #0bb09f;
    --blue: #0096d6;
    --blue-icon: #1f7fd0;
    --pink-dot: #f9dcea;
    --ink: #1b1b1b;
    --white: #ffffff;
    --illustration: #7d9fd6;
    --portrait: #8a6a62;
  }
  html, body { margin: 0; padding: 0; overflow: hidden; background: var(--paper); }
  .flyer {
    position: relative;
    width: 710px;
    height: 1200px;
    overflow: hidden;
    background: var(--paper);
    font-family: "Poppins", sans-serif;
  }
  .shape { position: absolute; inset: 0; width: 710px; height: 1200px; }
  .brand-mark {
    position: absolute;
    left: 30px; top: 40px;
    width: 140px;
    text-align: center;
    font-family: "Poppins", sans-serif;
    font-weight: 500;
    font-size: 17px;
    line-height: 1.25;
    color: var(--ink);
  }
  .intro {
    position: absolute;
    left: 330px; top: 58px;
    width: 360px;
    color: var(--white);
  }
  .intro-title {
    margin: 0 0 4px 0;
    font-family: "Kalam", cursive;
    font-weight: 700;
    font-size: 26px;
    line-height: 1.2;
    display: flex;
    align-items: center;
    gap: 14px;
  }
  .intro-title::before {
    content: "";
    width: 10px; height: 10px;
    border-radius: 50%;
    background: var(--white);
    flex: none;
  }
  .intro-text {
    margin: 0;
    font-size: 17.5px;
    line-height: 30px;
    font-weight: 400;
  }
  .portrait {
    position: absolute;
    left: 90px; top: 338px;
    width: 226px; height: 226px;
    border-radius: 50%;
    border: 5px solid var(--blue);
    background: radial-gradient(circle at 50% 40%, #b08878 0%, var(--portrait) 45%, #5c5f66 100%);
    box-sizing: border-box;
  }
  .rates-band {
    position: absolute;
    left: 22px; top: 618px;
    width: 356px; height: 87px;
    background: var(--blue);
    color: var(--white);
    font-family: "Kalam", cursive;
    font-weight: 700;
    font-size: 27px;
    display: flex; align-items: center; justify-content: center;
  }
  .contact-list {
    position: absolute;
    left: 16px; top: 740px;
    width: 377px;
    margin: 0; padding: 0;
    list-style: none;
    text-align: center;
    color: var(--white);
    font-family: "Montserrat", sans-serif;
    font-weight: 600;
  }
  .contact-item { height: 118px; display: flex; flex-direction: column; align-items: center; }
  .contact-icon {
    width: 42px; height: 42px;
    border-radius: 50%;
    background: var(--pink-dot);
    display: flex; align-items: center; justify-content: center;
  }
  .contact-value { margin-top: 14px; font-size: 21px; line-height: 1.2; }
  .contact-value.email { font-size: 19px; }
  .meeting-illustration {
    position: absolute;
    left: 415px; top: 644px;
    width: 260px; height: 346px;
    border-radius: 18px;
    background: linear-gradient(180deg, #6a90d2 0%, var(--illustration) 55%, #a9b9d6 100%);
  }
  .sign-off {
    position: absolute;
    left: 425px; top: 1078px;
    width: 240px;
    text-align: center;
    color: var(--ink);
  }
  .sign-off-name { font-size: 20px; font-weight: 400; line-height: 1.2; }
  .sign-off-tag { font-size: 10px; font-weight: 500; margin-top: 4px; }
</style>
</head>
<body>
<main class="flyer">
  <svg class="shape" viewBox="0 0 710 1200" aria-hidden="true">
    <path class="intro-blob" fill="var(--green-deep)"
      d="M380 0 H710 V402 C640 420 540 428 450 398 C340 362 250 292 258 192 C265 100 320 38 380 0 Z"/>
    <path class="contact-blob" fill="var(--green-bright)"
      d="M55 598 C120 560 300 558 358 582 C386 622 393 700 393 800 L390 1100 C386 1140 360 1152 320 1146 C250 1140 200 1176 120 1166 C40 1156 16 1100 16 1020 L18 720 C20 662 32 620 55 598 Z"/>
  </svg>

  <div class="brand-mark">Teodric F. Morvantelk</div>

  <section class="intro">
    <h2 class="intro-title">What is Mediation?</h2>
    <p class="intro-text">Mediation is a form of facilitated negotiation, by a mediator, who helps the parties engage in a dialog to search for a joint agreement. All decisions, from agreeing to participate in the mediation, to possible terms of an agreement,</p>
  </section>

  <div class="portrait" role="img" aria-label="Portrait photograph of the mediator"></div>

  <div class="rates-band">Sliding scale rates available</div>

  <ul class="contact-list">
    <li class="contact-item">
      <span class="contact-icon">
        <svg width="24" height="24" viewBox="0 0 24 24" aria-hidden="true"><path fill="var(--blue-icon)" d="M6.6 10.8a15.1 15.1 0 0 0 6.6 6.6l2.2-2.2a1 1 0 0 1 1-.25 11.4 11.4 0 0 0 3.6.57 1 1 0 0 1 1 1V20a1 1 0 0 1-1 1A17 17 0 0 1 3 4a1 1 0 0 1 1-1h3.5a1 1 0 0 1 1 1c0 1.25.2 2.45.57 3.57a1 1 0 0 1-.25 1z"/></svg>
      </span>
      <span class="contact-value">+1.555.384.7290</span>
    </li>
    <li class="contact-item">
      <span class="contact-icon">
        <svg width="26" height="20" viewBox="0 0 26 20" aria-hidden="true" fill="none" stroke="var(--blue-icon)" stroke-width="1.8"><rect x="2" y="2" width="22" height="16"/><path d="M2 2 L13 11 L24 2 M2 18 L10 9 M24 18 L16 9"/></svg>
      </span>
      <span class="contact-value email">teodric@morvantelkresolve.com</span>
    </li>
    <li class="contact-item">
      <span class="contact-icon">
        <svg width="26" height="26" viewBox="0 0 26 26" aria-hidden="true" fill="none" stroke="var(--blue-icon)" stroke-width="1.6"><circle cx="13" cy="13" r="10"/><ellipse cx="13" cy="13" rx="4.5" ry="10"/><path d="M3 13 H23 M5 7.5 H21 M5 18.5 H21 M13 3 V23"/></svg>
      </span>
      <span class="contact-value">www.morvantelkresolve.com</span>
    </li>
  </ul>

  <div class="meeting-illustration" role="img" aria-label="Illustration of three people seated around a table in a meeting"></div>

  <div class="sign-off">
    <div class="sign-off-name">Teodric F. Morvantelk</div>
    <div class="sign-off-tag">Alternative Dispute Resolution</div>
  </div>
</main>
</body>
</html>
```